Brochure Design Project

1.We need a brochure design for our event program and invitation.

2.We must be able to print out the brochure and also send it out via email to participants.

3.We want the whole design to relate to "Cross-Examination","International Arbitration" atmosphere.

4.We want the design to look a bit (but not too) fancy and be readable.

Reason: There are only 2 of 6 designs we like. But we still need more options to choose.

Target Market(s)

Our audiences are all Chinese and International Lawyers

Industry/Entity Type

Event

Requirements
Must have
• 1. The brochure needs to actually reflect “cross-examination” on the cover. The title should go at the top of the page.

2. The brochure needs to make room for organizers and supporters’ logo. This is a cooperation event.

3. It is important that the text is a big enough to be read easily. At the moment we have been using Helvetica font at size 9 or 10. Helvetica is easily readable at this size.

4. The brochure color needs to be in line with our logo color, such as Green-Blue and white. Please suggest a color that also fits the organizers’ logo.

5. We need a pdf version and print out version. They are all A4 size. The pdf version size must be under 2 MB. Otherwise it’s difficult to send out as well as receive. For the printing version, when designing you need to leave a 4mm bleed over the page size. This bleed is important - otherwise the picture will not necessarily go to the edge of the cut. You also need to make sure that the text is not too close to the boundary. I tend to leave a 4-5mm margin for text within this on all sides.

6. Use the same font style as suggested in the draft program and invitation.
Nice to have
• A picture which represents the idea of cross-examination. I will send you the example pic.
Should not have
• 1. Should not be aggressive;

2. Should not be too fancy or too conservative;

3. Should not be too colorful

```html
<!DOCTYPE html>
<html lang="en">
<head>
<meta charset="utf-8">
<title>Workshop Program</title>
<link rel="stylesheet" href="https://fonts.googleapis.com/css2?family=Inter:wght@300;400&display=swap">
<style>
  :root {
    --brand-blue: #0066b3;
    --date-red: #8a1414;
    --body-grey: #555555;
    --page-white: #ffffff;
  }
  * { margin: 0; padding: 0; box-sizing: border-box; }
  html, body {
    width: 1200px;
    height: 851px;
    overflow: hidden;
    background: var(--page-white);
  }
  .spread {
    position: relative;
    width: 1200px;
    height: 851px;
    background: var(--page-white);
    font-family: "Inter", Helvetica, Arial, sans-serif;
    font-weight: 300;
    color: var(--body-grey);
  }
  .edge-tab {
    position: absolute;
    top: 142px;
    height: 97px;
    background: var(--brand-blue);
  }
  .edge-tab--left { left: 0; width: 41px; }
  .edge-tab--right { right: 0; width: 43px; }

  .program {
    position: absolute;
    left: 638px;
    top: 137px;
    width: 480px;
  }
  .program__title {
    font-size: 25px;
    font-weight: 300;
    color: var(--brand-blue);
    letter-spacing: -0.2px;
    line-height: 30px;
  }
  .program__note {
    margin-top: 23px;
    font-size: 11.2px;
    line-height: 14px;
  }
  .day {
    margin-top: 31px;
  }
  .day + .day { margin-top: 22px; }
  .day__date {
    font-size: 14px;
    font-weight: 400;
    color: var(--date-red);
    line-height: 18px;
    margin-bottom: 5px;
  }
  .session {
    display: flex;
    font-size: 11.2px;
    line-height: 21.2px;
  }
  .session__time { width: 81px; flex: none; }
</style>
</head>
<body>
<main class="spread">
  <div class="edge-tab edge-tab--left"></div>
  <div class="edge-tab edge-tab--right"></div>

  <section class="program">
    <h1 class="program__title">Program</h1>
    <p class="program__note">This workshop will be conducted in English.</p>

    <div class="day">
      <h2 class="day__date">10 December 2012</h2>
      <div class="session"><span class="session__time">8:30-9:00</span><span>Registration</span></div>
      <div class="session"><span class="session__time">9:00-9:15</span><span>Introductory words by Halden Group and KellerARB</span></div>
      <div class="session"><span class="session__time">9:15-9:25</span><span>Demonstration of direct examination</span></div>
      <div class="session"><span class="session__time">9:25-9:45</span><span>Demonstration of cross-examination</span></div>
      <div class="session"><span class="session__time">9:45-10:15</span><span>Case strategy: Preparation for cross</span></div>
      <div class="session"><span class="session__time">10:15-10:30</span><span>Coffee Break</span></div>
      <div class="session"><span class="session__time">10:30-12:00</span><span>Exercises in classic cross-examination</span></div>
      <div class="session"><span class="session__time">12:00-12:15</span><span>Instructor and student observations on exercises</span></div>
      <div class="session"><span class="session__time">12:15-13:15</span><span>Lunch</span></div>
      <div class="session"><span class="session__time">13:15-14:45</span><span>Exercises in classic cross-examination</span></div>
      <div class="session"><span class="session__time">14:45-15:00</span><span>Coffee Break</span></div>
      <div class="session"><span class="session__time">15:00-15:30</span><span>Demonstration of cross-examination of experts</span></div>
      <div class="session"><span class="session__time">15:30-17:30</span><span>Exercises in expert cross-examination</span></div>
      <div class="session"><span class="session__time">19.00-21:30</span><span>Joint dinner sponsored by KellerARB</span></div>
    </div>

    <div class="day">
      <h2 class="day__date">11 December 2012</h2>
      <div class="session"><span class="session__time">9:00-10:30</span><span>Repeat weak spots, dealing with different panels</span></div>
      <div class="session"><span class="session__time">10:30-10:50</span><span>Demonstration of “hot-tubbing” expert witnesses</span></div>
      <div class="session"><span class="session__time">10:50-11:00</span><span>Coffee Break</span></div>
      <div class="session"><span class="session__time">11:00-12:30</span><span>Exercises in expert cross-examination</span></div>
    </div>
  </section>
</main>
</body>
</html>
```